RT Penbrook, LLC Business Card

I want a two-sided business card that provides people with our contact information, our mission, and a sample of our services. I would love a QR code somewhere on the card linking to our website if possible (www.rtpenbrookco.example).
Mission:
To help social service organizations develop a Mission Aligned Data Driven mindset that promotes positive change in the lives of the customers they serve.
Services:
Consulting
Training
Community Assessment Development
Strategic Planning
Report Development
Data Analytics
(Note: the website domain is currently mid-transfer so you can't see it at the link we want on the card. You can, however, view it for reference at https://rtpenbrookco.blogsite.example/)
Contact Information for Business Card
Name: Derek Penbrook, NCRT/MT
Title: Chief Executive Officer
Address: 4178 Larch Lane, Cumming, Georgia 30041
Telephone: (706) 555-0184
Email: derek@rtpenbrookco.example
Colors
Designer to choose colors to be used in the design.
Look and feel

```html
<!DOCTYPE html>
<html lang="en">
<head>
<meta charset="utf-8">
<title>RT Penbrook, LLC — Business Card</title>
<link rel="stylesheet" href="https://fonts.googleapis.com/css2?family=Lato:wght@300;400;700;900&display=swap">
<style>
  :root {
    --stage: #1b1b1b;
    --card-dark: #141414;
    --card-light: #ffffff;
    --ink-light: #f2f2f2;
    --ink-dark: #3a3a3a;
    --accent: #2a9fd8;
    --rule-dark: #5a5a5a;
    --rule-light: #c9c9c9;
    --rule-brand: #4a4a4a;
  }
  * { box-sizing: border-box; margin: 0; padding: 0; }
  html, body {
    width: 1200px; height: 900px; overflow: hidden;
    background: var(--stage);
    font-family: "Lato", Arial, sans-serif;
  }
  .stage {
    width: 1200px; height: 900px;
    display: flex; flex-direction: column;
    align-items: center; justify-content: center; gap: 56px;
  }
  .card {
    width: 580px; height: 331px;
    position: relative;
    box-shadow: 0 12px 30px rgba(0,0,0,.55);
  }

  /* Back side */
  .card--back { background: var(--card-dark); color: var(--ink-light); }
  .brand-back {
    position: absolute; top: 92px; left: 0; right: 0;
    display: flex; align-items: center; justify-content: center; gap: 14px;
  }
  .brand-back__dot {
    width: 34px; height: 34px; border-radius: 50%;
    background: linear-gradient(160deg, #f4f4f4, #7d7d7d);
  }
  .brand-back__name {
    font-size: 30px; font-weight: 700; letter-spacing: .06em;
    color: var(--ink-light); text-transform: uppercase;
  }
  .services {
    position: absolute; left: 38px; right: 38px; bottom: 38px;
    border-top: 1px solid var(--rule-dark);
    padding-top: 12px;
    font-size: 16.5px; font-weight: 400; line-height: 1.32;
    text-align: center;
  }
  .services__bullet {
    display: inline-block; width: 8px; height: 8px; border-radius: 50%;
    background: var(--ink-light); margin: 0 6px; vertical-align: middle;
  }

  /* Front side */
  .card--front { background: var(--card-light); color: var(--ink-dark); }
  .brand-front {
    position: absolute; left: 30px; top: 148px; width: 218px;
  }
  .brand-front__lockup {
    display: flex; align-items: center; gap: 10px;
  }
  .brand-front__dot {
    width: 36px; height: 36px; border-radius: 50%; background: var(--accent); flex: none;
  }
  .brand-front__name {
    font-size: 22px; font-weight: 700; letter-spacing: .02em;
    color: var(--accent); text-transform: uppercase; white-space: nowrap;
  }
  .brand-front__rule {
    margin: 6px 0 0 46px; height: 1px; background: var(--rule-brand);
  }
  .divider {
    position: absolute; left: 268px; top: 52px; bottom: 52px;
    width: 1px; background: var(--rule-light);
  }
  .contact {
    position: absolute; left: 290px; top: 56px; right: 20px;
  }
  .contact__name {
    font-size: 17px; font-weight: 900; color: var(--accent);
    text-transform: uppercase; letter-spacing: .02em;
  }
  .contact__cred {
    font-size: 12px; font-weight: 400; color: var(--accent);
  }
  .contact__title { font-size: 15px; color: var(--ink-dark); margin-bottom: 16px; }
  .contact__row {
    display: flex; align-items: center; gap: 7px;
    font-size: 15px; line-height: 1.4; color: var(--ink-dark);
  }
  .contact__row svg { width: 13px; height: 13px; flex: none; }
  .contact__address {
    margin-top: 14px; font-size: 15px; line-height: 1.35; color: var(--ink-dark);
  }
</style>
</head>
<body>
<main class="stage">

  <section class="card card--back" aria-label="Business card, back">
    <div class="brand-back">
      <span class="brand-back__dot"></span>
      <span class="brand-back__name">RT Penbrook</span>
    </div>
    <p class="services">
      Consulting<span class="services__bullet"></span>Training<span class="services__bullet"></span>Community Assessment Development<br>
      Strategic Planning<span class="services__bullet"></span>Report Development<span class="services__bullet"></span>Data Analytics
    </p>
  </section>

  <section class="card card--front" aria-label="Business card, front">
    <div class="brand-front">
      <div class="brand-front__lockup">
        <span class="brand-front__dot"></span>
        <span class="brand-front__name">RT Penbrook</span>
      </div>
      <div class="brand-front__rule"></div>
    </div>

    <div class="divider"></div>

    <div class="contact">
      <p class="contact__name">Derek Penbrook<span class="contact__cred">, NCRT/MT</span></p>
      <p class="contact__title">Chief Executive Officer</p>

      <p class="contact__row">
        <svg viewBox="0 0 16 16" aria-hidden="true"><path fill="#2a9fd8" d="M3.6 1.5l2.3 2.4-1.3 1.9c.9 2 2.6 3.7 4.6 4.6l1.9-1.3 2.4 2.3-1.6 2.6C6.6 13.6 2.4 9.4 1 4.1z"/></svg>
        (706) 555-0184
      </p>
      <p class="contact__row">
        <svg viewBox="0 0 16 16" aria-hidden="true"><rect x="1" y="3" width="14" height="10" rx="1" fill="#2a9fd8"/><path d="M1.5 3.8L8 9l6.5-5.2" stroke="#fff" stroke-width="1.3" fill="none"/></svg>
        derek@rtpenbrookco.example
      </p>
      <p class="contact__row">
        <svg viewBox="0 0 16 16" aria-hidden="true"><circle cx="8" cy="8" r="7" fill="#2a9fd8"/><path d="M1 8h14M8 1c-2.6 3-2.6 11 0 14M8 1c2.6 3 2.6 11 0 14" stroke="#fff" stroke-width="1" fill="none"/></svg>
        www.rtpenbrookco.example
      </p>

      <p class="contact__address">4178 Larch Lane<br>Cumming, Georgia 30041</p>
    </div>
  </section>

</main>
</body>
</html>
```